Social Health & Parkinson's

I need a 1-pg horizontal infographic that can be handed out to patients and providers. It needs to be scientifically sound (data provided), easy to understand, and visually pleasing. Target audience; patiens (mostly 40-90 years old) and providers (neurologists, nurses, physical therapists, naturopathic physicians, support group leaders, etc.) We need 6 of these, one for each topic listed on the website. Ideally, we'll hire the winner for 5 more similar projects and keep a theme.

Target Market(s)

Patients with Parkinson's disease, their families, care providers. To be handed out by physicians, support group leaders, etc.

Colors

Designer to choose colors to be used in the design.

Requirements
Must have
• Visually stunning. Data integrity-- keep the numbers and the figures we provide. Reference to where the data is coming from. Be thoughtful of elderly, vision issues. Teach everyone something.

```html
<!DOCTYPE html>
<html lang="en">
<head>
<meta charset="utf-8">
<title>Social Health &amp; Patient Reported Outcomes in PD</title>
<link rel="stylesheet" href="https://fonts.googleapis.com/css2?family=Cambo&family=Kalam:wght@300;400&family=Lato:wght@400;700&display=swap">
<style>
  :root {
    --yellow: #dfe10c;
    --mint: #68ffae;
    --sky: #a2e9fb;
    --lavender: #d9b6e6;
    --sand: #e8cfa4;
    --ink: #111111;
    --deep-red: #b00d0d;
    --rose: #e23a5c;
    --white: #ffffff;
  }
  * { box-sizing: border-box; margin: 0; padding: 0; }
  html, body { width: 1200px; height: 893px; overflow: hidden; background: var(--white); }
  .infographic { position: relative; width: 1200px; height: 893px; font-family: "Lato", sans-serif; }
  .title {
    position: absolute; left: 0; width: 1200px; top: 36px; text-align: center;
    font-family: "Cambo", serif; font-weight: 400; font-size: 39px; line-height: 45px;
    letter-spacing: 3px; color: var(--ink);
  }
  .tagline {
    position: absolute; left: 0; width: 1200px; top: 128px; text-align: center;
    font-family: "Kalam", cursive; font-weight: 300; font-size: 16px; letter-spacing: 0.3px;
    color: var(--rose);
  }
  .rings { position: absolute; left: 0; top: 0; width: 1200px; height: 893px; }
  .fact {
    position: absolute; border-radius: 44px; color: var(--white); white-space: nowrap;
    font-weight: 400; font-size: 17px; line-height: 20.5px; letter-spacing: -0.4px;
    text-shadow: 0 0 1px rgba(0,0,0,0.18);
  }
  .fact--friends { left: 46px; top: 236px; width: 406px; height: 189px; background: var(--yellow); padding: 35px 20px 0 41px; }
  .fact--lonely { left: 50px; top: 553px; width: 381px; height: 192px; background: var(--mint); padding: 34px 20px 0 51px; }
  .takeaway {
    position: absolute; border-radius: 52px; background: var(--white); white-space: nowrap;
    color: var(--deep-red); font-size: 17.5px; line-height: 20.5px;
  }
  .takeaway--tremor { left: 891px; top: 236px; width: 267px; height: 176px; border: 12px solid var(--yellow); padding: 20px 0 0 20px; }
  .takeaway--lonely { left: 893px; top: 576px; width: 259px; height: 138px; border: 10px solid var(--mint); padding: 22px 0 0 0; text-align: center; }
  .divider { position: absolute; left: 182px; top: 826px; width: 835px; height: 4px; background: var(--mint); }
  .site {
    position: absolute; left: 0; width: 1200px; top: 843px; text-align: center;
    font-weight: 400; font-size: 16.5px; color: var(--mint);
  }
</style>
</head>
<body>
<main class="infographic">
  <h1 class="title">Social Health &amp; Patient<br>Reported Outcomes in PD</h1>
  <p class="tagline">Rx: Nurture social health. Make friends. Avoid loneliness</p>

  <svg class="rings" viewBox="0 0 1200 893">
    <defs>
      <radialGradient id="friends-scene" cx="50%" cy="55%" r="60%">
        <stop offset="0" stop-color="var(--lavender)"/>
        <stop offset="0.45" stop-color="#bfe3f3"/>
        <stop offset="1" stop-color="var(--sky)"/>
      </radialGradient>
      <radialGradient id="lonely-scene" cx="45%" cy="65%" r="60%">
        <stop offset="0" stop-color="var(--sand)"/>
        <stop offset="0.4" stop-color="#c7dfe9"/>
        <stop offset="1" stop-color="var(--sky)"/>
      </radialGradient>
    </defs>
    <path class="ring ring--lonely" d="M691 497 A146 146 0 1 0 761 691" fill="none" stroke="var(--mint)" stroke-width="46"/>
    <circle cx="640" cy="629" r="124" fill="url(#lonely-scene)" role="img" aria-label="Illustration of a lonely man sitting hunched on boxes"/>
    <path class="ring ring--friends" d="M544 345 A147 147 0 1 1 641 483" fill="none" stroke="var(--yellow)" stroke-width="46"/>
    <circle cx="689" cy="345" r="122" fill="url(#friends-scene)" role="img" aria-label="Illustration of a group of older friends and a person in a wheelchair with health and care symbols"/>
  </svg>

  <p class="fact fact--friends">Individuals that reported having a lot of friends<br>had reduced PD severity scores (168; p=0.000).<br>Notably, exercising 7 days per week was less<br>beneficial (301; p=0.000) than feeling lonely<br>was detrimental.</p>

  <p class="takeaway takeaway--tremor">Although tremor is a cardinal<br>symptom of PD and highly<br>visible, feeling socially with-<br>drawn is more closely<br>correlated to overall quality<br>of life than tremor</p>

  <p class="fact fact--lonely">Individuals who reported feeling lonely<br>reported greater overall PD symptom<br>severity (+328; p=0.000), which was even<br>higher than scores for smoking tobacco<br>(+173; p=0.005) and having a lot of stress<br>(+180; p=0.000).</p>

  <p class="takeaway takeaway--lonely">Overall, individuals<br>identifying as being lonely<br>reported consistently greater<br>PD symptom severity.</p>

  <div class="divider"></div>
  <p class="site">www.ThrivingWithPDExample.org</p>
</main>
</body>
</html>
```